Harborline Crest Insurance Services

we are a high end insurance agency we specialize on Auto | Home | Business | Life looking for something professional and luxuries at the same time. if you guys need anything else please let me know.

Auto | Home | Business | Life must be under logo on the back with black background.

i want the back part to be black with our gold logo on it.

Target Market(s)

Auto | Home | Business | Life

Industry/Entity Type

Insurance Broker

Contact Information for Business Card

My logo is gold so a black in the back would be nice.

Font styles to use
Serif

Colors
000000

Requirements
Must have
• Big logo on the back with black background.

```html
<!DOCTYPE html>
<html lang="en">
<head>
<meta charset="utf-8">
<title>Harborline Crest Insurance Services – Business Card</title>
<link href="https://fonts.googleapis.com/css2?family=Cinzel:wght@600&family=Tinos:wght@700&family=Open+Sans:wght@400;600&display=swap" rel="stylesheet">
<style>
  :root {
    --stage: #e8e5e1;
    --card-black: #050505;
    --gold: #f2c12e;
    --gold-deep: #e6b21f;
    --white: #ffffff;
    --ink: #111111;
    --skyline-top: #070707;
    --skyline-bottom: #101010;
  }
  * { margin: 0; padding: 0; box-sizing: border-box; }
  html, body {
    width: 1200px;
    height: 900px;
    overflow: hidden;
    background: var(--stage);
  }
  .canvas { position: relative; width: 1200px; height: 900px; }

  .card {
    position: absolute;
    background: var(--card-black);
    overflow: hidden;
    box-shadow: 0 6px 18px rgba(0,0,0,0.25);
  }

  .brand-mark {
    position: absolute;
    border-radius: 50%;
    background: var(--gold);
  }
  .brand-name {
    position: absolute;
    font-family: "Cinzel", serif;
    font-weight: 600;
    color: var(--gold);
    text-align: center;
    line-height: 1.25;
  }

  /* Front */
  .card-front { left: 78px; top: 33px; width: 587px; height: 364px; }
  .front-sweep { position: absolute; inset: 0; }
  .card-front .brand-mark { left: 97px; top: 42px; width: 70px; height: 70px; }
  .card-front .brand-name { left: 22px; top: 124px; width: 220px; font-size: 19px; }

  .holder { position: absolute; right: 36px; top: 48px; width: 180px; }
  .holder-name {
    font-family: "Tinos", serif;
    font-weight: 700;
    font-size: 21px;
    color: var(--ink);
    letter-spacing: 0.3px;
  }
  .holder-title {
    font-family: "Open Sans", sans-serif;
    font-size: 15px;
    color: var(--ink);
    margin-top: 1px;
  }
  .contact {
    position: absolute;
    left: 29px;
    font-family: "Open Sans", sans-serif;
    font-size: 14.5px;
    color: var(--white);
    white-space: nowrap;
  }
  .contact-address { top: 243px; }
  .contact-phones { top: 287px; }
  .contact-web { top: 314px; }
  .contact .label { color: var(--gold); font-weight: 600; }
  .contact .gap { display: inline-block; width: 16px; }
  .contact .site { color: var(--gold); font-weight: 600; }

  /* Back */
  .card-back { left: 388px; top: 505px; width: 565px; height: 352px; }
  .skyline-band { position: absolute; left: 0; right: 0; bottom: 0; height: 105px; }
  .card-back .brand-mark { left: 222px; top: 58px; width: 120px; height: 120px; }
  .card-back .brand-name { left: 0; right: 0; top: 196px; font-size: 25px; }
  .services {
    position: absolute;
    left: 0; right: 0; top: 290px;
    text-align: center;
    font-family: "Cinzel", serif;
    font-weight: 600;
    font-size: 16px;
    color: var(--gold);
    letter-spacing: 0.5px;
  }
  .services li { display: inline; list-style: none; margin: 0 3px; }
  .services li::before {
    content: "";
    display: inline-block;
    width: 8px; height: 8px;
    border-radius: 50%;
    background: var(--gold);
    margin-right: 5px;
    vertical-align: 2px;
  }
</style>
</head>
<body>
<main class="canvas">

  <section class="card card-front" aria-label="Business card front">
    <svg class="front-sweep" width="587" height="364" viewBox="0 0 587 364" aria-hidden="true">
      <defs>
        <linearGradient id="sweepGold" x1="0" y1="0" x2="1" y2="1">
          <stop offset="0" stop-color="#f2c12e"/>
          <stop offset="1" stop-color="#e6b21f"/>
        </linearGradient>
      </defs>
      <path d="M272 0 C 268 150 360 300 497 364 L587 364 L587 0 Z" fill="url(#sweepGold)"/>
    </svg>

    <span class="brand-mark" aria-hidden="true"></span>
    <p class="brand-name">Harborline Crest<br>Insurance Services</p>

    <div class="holder">
      <p class="holder-name">DANIEL REEVES</p>
      <p class="holder-title">Managing Director</p>
    </div>

    <p class="contact contact-address">1234, Address GoesHere, Country, 12345</p>
    <p class="contact contact-phones"><span class="label">P:</span> (044) 555 018 274<span class="gap"></span><span class="label">M:</span> (044)555093461</p>
    <p class="contact contact-web"><span class="label">E:</span> hello@harborlinecrest.com&nbsp; <span class="site">www.harborlinecrest.com</span></p>
  </section>

  <section class="card card-back" aria-label="Business card back">
    <svg class="skyline-band" width="565" height="105" viewBox="0 0 565 105" role="img" aria-label="Faint embossed city skyline along the bottom edge">
      <defs>
        <linearGradient id="skylineShade" x1="0" y1="0" x2="0" y2="1">
          <stop offset="0" stop-color="#070707"/>
          <stop offset="1" stop-color="#101010"/>
        </linearGradient>
      </defs>
      <rect width="565" height="105" fill="url(#skylineShade)"/>
    </svg>

    <span class="brand-mark" aria-hidden="true"></span>
    <p class="brand-name">Harborline Crest<br>Insurance Services</p>

    <ul class="services">
      <li>AUTO</li><li>HOME</li><li>BUSINESS</li><li>LIFE</li>
    </ul>
  </section>

</main>
</body>
</html>
```